Velmira Body Oil Label for 4 -8 oz bottles

We are selling 4 and 8 oz body oils and need a label to put on our bottles. I'm not sure if we want a label for the front and also the back of the bottle or just one label in the front. You can give me examples of each way. Attached is our logo on a blue background but the background will change colors depending on the scent as specified in the design description. Our bottle will be either clear or white with a pump spray type lid as shown in the attached example. Attached are also our design criteria which is needed for the labels.
Updates

We have decided to use the disc top cap and not the pump spray cap. If you are able to, please show us the design on the 4 oz bottle with the disc top cap. Thanks

Target Market(s)

women

Industry/Entity Type

skincare, cosmetics

Font styles to use
Serif
Sans Serif

Requirements
Must have
• stylish name for each scented oil which contrasts the font in the logo. Also must have darker colors since the logo colors are lighter.
Nice to have
• Border around the labels, maybe one solid color or maybe two complimenting colors which go well with the fragrnace name
Should not have
• background colors that match the logo colors

```html
<!DOCTYPE html>
<html lang="en">
<head>
<meta charset="utf-8">
<title>Velmira Body Oil Labels</title>
<link href="https://fonts.googleapis.com/css2?family=Barlow:wght@400;500;600&family=Oswald:wght@500&display=swap" rel="stylesheet">
<style>
  :root {
    --page: #ffffff;
    --ink-light: #ffffff;
    --pink: #e3207f;
    --pink-light: #f07ab4;
    --pink-accent: #4db3b8;
    --purple: #5a17d6;
    --purple-light: #a56ef0;
    --purple-accent: #3a1a92;
    --green: #1e5a1f;
    --green-light: #6fa56a;
    --green-accent: #23237f;
    --red: #df2c36;
    --red-light: #ef6d72;
    --red-accent: #f29b1e;
  }
  * { box-sizing: border-box; margin: 0; padding: 0; }
  html, body { width: 1200px; height: 669px; overflow: hidden; background: var(--page); }
  body { font-family: "Barlow", Arial, sans-serif; color: var(--ink-light); }

  .label-row {
    display: flex;
    justify-content: center;
    gap: 48px;
    padding-top: 28px;
  }
  .label {
    position: relative;
    width: 250px;
    height: 612px;
    overflow: hidden;
    background: linear-gradient(100deg, var(--tone-light) 0%, var(--tone) 38%, var(--tone) 100%);
  }
  .label--cotton-candy { --tone: var(--pink); --tone-light: var(--pink-light); --accent: var(--pink-accent); }
  .label--lavender { --tone: var(--purple); --tone-light: var(--purple-light); --accent: var(--purple-accent); }
  .label--lavender-green { --tone: var(--green); --tone-light: var(--green-light); --accent: var(--green-accent); }
  .label--fruity-delight { --tone: var(--red); --tone-light: var(--red-light); --accent: var(--red-accent); }

  .brand {
    position: absolute;
    top: 88px; left: 0; right: 0;
    display: flex; align-items: center; justify-content: center; gap: 10px;
  }
  .brand-dot { width: 14px; height: 14px; border-radius: 50%; background: var(--ink-light); }
  .brand-name {
    font-family: "Barlow", Arial, sans-serif;
    font-weight: 400;
    font-size: 44px;
    letter-spacing: 2px;
    color: var(--ink-light);
  }

  .scent-name {
    position: absolute;
    top: 190px; left: 0; right: 0;
    text-align: center;
    font-family: "Oswald", "Arial Narrow", sans-serif;
    font-weight: 500;
    font-size: 45px;
    line-height: 1;
    letter-spacing: -0.5px;
  }
  .wave { position: absolute; top: 250px; left: 20px; width: 210px; height: 16px; }
  .drop { position: absolute; top: 282px; left: 113px; width: 24px; height: 34px; }

  .usage {
    position: absolute;
    top: 325px; left: 0; right: 0;
    text-align: center;
    font-size: 14.5px;
    line-height: 19.5px;
    font-weight: 400;
    opacity: 0.9;
  }

  .benefits {
    position: absolute;
    top: 405px; left: 16px; right: 16px;
    display: flex; justify-content: space-between; align-items: center;
  }
  .benefit {
    width: 58px; height: 88px;
    border-radius: 29px / 38px;
    background: var(--accent);
    display: flex; align-items: center; justify-content: center;
    text-align: center;
    font-size: 10px; line-height: 12px; font-weight: 600;
    opacity: 0.9;
  }
  .benefit--main { width: 74px; height: 90px; border-radius: 37px / 40px; opacity: 1; }

  .ingredients {
    position: absolute;
    top: 512px; left: 12px; right: 12px;
    text-align: center;
    font-size: 6.6px; line-height: 10.5px;
  }
  .ingredients-title { font-weight: 600; font-size: 8px; margin-bottom: 1px; }

  .net-weight {
    position: absolute;
    bottom: 0; left: 0; right: 0;
    height: 30px;
    background: var(--accent);
    display: flex; align-items: center; justify-content: center;
    font-size: 12.5px;
  }
</style>
</head>
<body>
<main class="label-row">

  <section class="label label--cotton-candy">
    <div class="brand"><span class="brand-dot"></span><span class="brand-name">Velmira</span></div>
    <h2 class="scent-name">Cotton Candy</h2>
    <svg class="wave" viewBox="0 0 210 16"><path d="M2 8 Q55 0 105 8 T208 8" fill="none" stroke="#ffffff" stroke-width="1.5"/></svg>
    <svg class="drop" viewBox="0 0 24 34"><path d="M12 1 C16 10 23 17 23 23 A11 11 0 0 1 1 23 C1 17 8 10 12 1 Z" fill="var(--accent)"/></svg>
    <p class="usage">Apply a small amount to skin<br>and massage until absorbed.<br>Use daily for best results.</p>
    <div class="benefits">
      <span class="benefit">Non-Greesy</span>
      <span class="benefit benefit--main">With<br>Vitamin E</span>
      <span class="benefit">Ultra<br>Moisturizing</span>
    </div>
    <div class="ingredients">
      <p class="ingredients-title">Ingredients</p>
      <p>Cocos Nucifera (Coconut) Oil, Prunus Amygdalus Dulcis (Almond) Oil, Vitis Vinifera (Grapeseed) Oil, Sesamum Indicum (Sesame) Seed Oil, Simmondsia Chinensis (Jojoba) Oil, Tocopheryl Acetate (Vitamin E) Essential oils, and fragrances.</p>
    </div>
    <div class="net-weight">Made in USA. Net Wt. 4 fl. oz. 118 mL</div>
  </section>

  <section class="label label--lavender">
    <div class="brand"><span class="brand-dot"></span><span class="brand-name">Velmira</span></div>
    <h2 class="scent-name">Soft Lavender</h2>
    <svg class="wave" viewBox="0 0 210 16"><path d="M2 8 Q55 0 105 8 T208 8" fill="none" stroke="#ffffff" stroke-width="1.5"/></svg>
    <svg class="drop" viewBox="0 0 24 34"><path d="M12 1 C16 10 23 17 23 23 A11 11 0 0 1 1 23 C1 17 8 10 12 1 Z" fill="var(--accent)"/></svg>
    <p class="usage">Apply a small amount to skin<br>and massage until absorbed.<br>Use daily for best results.</p>
    <div class="benefits">
      <span class="benefit">Non-Greesy</span>
      <span class="benefit benefit--main">With<br>Vitamin E</span>
      <span class="benefit">Ultra<br>Moisturizing</span>
    </div>
    <div class="ingredients">
      <p class="ingredients-title">Ingredients</p>
      <p>Cocos Nucifera (Coconut) Oil, Prunus Amygdalus Dulcis (Almond) Oil, Vitis Vinifera (Grapeseed) Oil, Sesamum Indicum (Sesame) Seed Oil, Simmondsia Chinensis (Jojoba) Oil, Tocopheryl Acetate (Vitamin E) Essential oils, and fragrances.</p>
    </div>
    <div class="net-weight">Made in USA. Net Wt. 4 fl. oz. 118 mL</div>
  </section>

  <section class="label label--lavender-green">
    <div class="brand"><span class="brand-dot"></span><span class="brand-name">Velmira</span></div>
    <h2 class="scent-name">Soft Lavender</h2>
    <svg class="wave" viewBox="0 0 210 16"><path d="M2 8 Q55 0 105 8 T208 8" fill="none" stroke="#ffffff" stroke-width="1.5"/></svg>
    <svg class="drop" viewBox="0 0 24 34"><path d="M12 1 C16 10 23 17 23 23 A11 11 0 0 1 1 23 C1 17 8 10 12 1 Z" fill="var(--accent)"/></svg>
    <p class="usage">Apply a small amount to skin<br>and massage until absorbed.<br>Use daily for best results.</p>
    <div class="benefits">
      <span class="benefit">Non-Greesy</span>
      <span class="benefit benefit--main">With<br>Vitamin E</span>
      <span class="benefit">Ultra<br>Moisturizing</span>
    </div>
    <div class="ingredients">
      <p class="ingredients-title">Ingredients</p>
      <p>Cocos Nucifera (Coconut) Oil, Prunus Amygdalus Dulcis (Almond) Oil, Vitis Vinifera (Grapeseed) Oil, Sesamum Indicum (Sesame) Seed Oil, Simmondsia Chinensis (Jojoba) Oil, Tocopheryl Acetate (Vitamin E) Essential oils, and fragrances.</p>
    </div>
    <div class="net-weight">Made in USA. Net Wt. 4 fl. oz. 118 mL</div>
  </section>

  <section class="label label--fruity-delight">
    <div class="brand"><span class="brand-dot"></span><span class="brand-name">Velmira</span></div>
    <h2 class="scent-name">Fruity Delight</h2>
    <svg class="wave" viewBox="0 0 210 16"><path d="M2 8 Q55 0 105 8 T208 8" fill="none" stroke="#ffffff" stroke-width="1.5"/></svg>
    <svg class="drop" viewBox="0 0 24 34"><path d="M12 1 C16 10 23 17 23 23 A11 11 0 0 1 1 23 C1 17 8 10 12 1 Z" fill="var(--accent)"/></svg>
    <p class="usage">Apply a small amount to skin<br>and massage until absorbed.<br>Use daily for best results.</p>
    <div class="benefits">
      <span class="benefit">Non-Greesy</span>
      <span class="benefit benefit--main">With<br>Vitamin E</span>
      <span class="benefit">Ultra<br>Moisturizing</span>
    </div>
    <div class="ingredients">
      <p class="ingredients-title">Ingredients</p>
      <p>Cocos Nucifera (Coconut) Oil, Prunus Amygdalus Dulcis (Almond) Oil, Vitis Vinifera (Grapeseed) Oil, Sesamum Indicum (Sesame) Seed Oil, Simmondsia Chinensis (Jojoba) Oil, Tocopheryl Acetate (Vitamin E) Essential oils, and fragrances.</p>
    </div>
    <div class="net-weight">Made in USA. Net Wt. 4 fl. oz. 118 mL</div>
  </section>

</main>
</body>
</html>
```